Tidal Oak Business Cards

We need something new, fun and exciting for business cards. Our current ones are just plain and we need a design that pops. We want name, position held, phone, email on the front, and a 20% discount on the back. I have also uploaded our old business cards creative to see what we are not wanting, and how boring they were and we want something jazzed up from this, cool design and catches people attention.

```html
<!DOCTYPE html>
<html lang="en">
<head>
<meta charset="utf-8">
<title>Tidal Oak Business Cards</title>
<link rel="stylesheet" href="https://fonts.googleapis.com/css2?family=Open+Sans:wght@400&family=Montserrat:wght@600&family=Roboto:wght@400&display=swap">
<style>
  :root {
    --backdrop: #e3e3e3;
    --navy: #1b3c6d;
    --coral: #ef6b6b;
    --white: #ffffff;
  }
  * { margin: 0; padding: 0; box-sizing: border-box; }
  html, body { width: 1200px; height: 1200px; overflow: hidden; background: var(--backdrop); }
  .canvas { position: relative; width: 1200px; height: 1200px; }
  .card { position: absolute; top: 265px; width: 377px; height: 659px; overflow: hidden; background: var(--white); }
  .card--back { left: 155px; }
  .card--front { left: 668px; }
  .card svg.card__shapes { position: absolute; inset: 0; }

  .offer { position: absolute; left: 0; top: 0; width: 377px; height: 659px; color: var(--coral);
    font-family: "Open Sans", sans-serif; font-weight: 400; }
  .offer__value, .offer__label { position: absolute; transform-origin: left bottom; transform: rotate(-21deg); white-space: nowrap; line-height: 1; }
  .offer__value { left: 102px; top: 300px; font-size: 84px; }
  .offer__label { left: 98px; top: 378px; font-size: 60px; letter-spacing: 1px; }

  .brand { position: absolute; top: 190px; left: 0; width: 377px; text-align: center; }
  .brand__dot { display: block; width: 22px; height: 22px; border-radius: 50%; background: var(--coral); margin: 0 auto 20px; }
  .brand__name { font-family: "Montserrat", sans-serif; font-weight: 600; font-size: 44px; color: var(--navy); letter-spacing: -0.5px; }

  .contacts { position: absolute; left: 52px; top: 454px; list-style: none;
    font-family: "Roboto", sans-serif; font-size: 20px; color: var(--white); }
  .contacts li { display: flex; align-items: center; height: 33.5px; }
  .contacts svg { width: 16px; height: 16px; margin-right: 12px; fill: var(--coral); flex: none; }
</style>
</head>
<body>
<div class="canvas">

  <section class="card card--back">
    <svg class="card__shapes" width="377" height="659" viewBox="0 0 377 659">
      <rect class="pattern" role="img" aria-label="Repeating pattern of coral heart, leaf and bow icons on navy" width="377" height="659" fill="var(--navy)"/>
      <g fill="var(--white)">
        <polygon points="0,255 60,225 150,205 230,185 300,170 377,178 377,455 320,470 240,490 160,505 100,512 40,520 0,510"/>
        <polygon points="20,190 180,172 250,160 210,180 60,198"/>
        <polygon points="200,505 330,480 377,470 377,478 290,498"/>
        <polygon points="0,340 20,345 0,350"/>
        <polygon points="350,330 377,325 377,332"/>
      </g>
    </svg>
    <div class="offer">
      <span class="offer__value">20%</span>
      <span class="offer__label">Discount</span>
    </div>
  </section>

  <section class="card card--front">
    <svg class="card__shapes" width="377" height="659" viewBox="0 0 377 659">
      <polygon class="pattern" role="img" aria-label="Repeating pattern of coral heart, leaf and bow icons on navy" fill="var(--navy)"
        points="0,0 377,0 377,62 330,75 250,95 180,110 110,128 130,150 60,150 0,158"/>
      <g fill="var(--navy)">
        <polygon points="0,425 80,408 170,395 240,372 200,358 290,360 377,370 377,659 0,659"/>
        <polygon points="190,350 300,345 260,354"/>
        <polygon points="30,398 130,390 90,398"/>
        <polygon points="300,122 318,121 318,124 300,125"/>
        <polygon points="280,650 340,640 377,645 377,659 300,659" fill="var(--white)"/>
        <polygon points="0,530 30,535 12,545 0,548" fill="var(--white)"/>
      </g>
    </svg>

    <div class="brand">
      <span class="brand__dot"></span>
      <span class="brand__name">Tidal Oak</span>
    </div>

    <ul class="contacts">
      <li><svg viewBox="0 0 16 16"><path d="M8 0a5.5 5.5 0 0 0-5.5 5.5C2.5 10 8 16 8 16s5.5-6 5.5-10.5A5.5 5.5 0 0 0 8 0zm0 8a2.5 2.5 0 1 1 0-5 2.5 2.5 0 0 1 0 5z"/></svg>123 Lorem, Ipsum, Country</li>
      <li><svg viewBox="0 0 16 16"><path d="M3.6 1l2.4 3-1.4 1.7c.9 2 2.6 3.8 4.7 4.7L11 9l3 2.4-1.5 2.8C7 14 2 9 1.8 3.3z"/></svg>+00 1234 6789 1478</li>
      <li><svg viewBox="0 0 16 16"><path d="M1 3h14v10H1zm1.5 1.2L8 8.6l5.5-4.4z" fill-rule="evenodd"/></svg>Lorem@company.com</li>
      <li><svg viewBox="0 0 16 16"><path d="M3 1l10 7-4.3.8L11 14l-2 1-2.3-5.2L3 13z"/></svg>www.websiteLorem.com</li>
    </ul>
  </section>

</div>
</body>
</html>
```